Verdant Loop Advisors, LLC

I am looking for a simple, clear layout with my logo prominent and embossed, on the best quality card stock available. I would like the business name and phone number included on the card as well......I dont want my name anywhere on the card and I would like my logo embossed on the card......something simple with a white back......open to designs as long as they go along with recycling symbols and green type stuff.....The address, website, cell number, fax number, and email are listed below

5374 Tillbury Fenwood Road
Larkfield, MD 20911

c. 240.555.0143 f. 240.555.0187
e. sales@verdantloopadvisors.example
w. www.verdantloopadvisors.example

Industry/Entity Type

Recycling

```html
<!DOCTYPE html>
<html lang="en">
<head>
<meta charset="utf-8">
<title>Verdant Loop Advisors, LLC – Business Card</title>
<link rel="stylesheet" href="https://fonts.googleapis.com/css2?family=Questrial&display=swap">
<style>
  :root {
    --card-white: #ffffff;
    --brand-green: #179719;
    --ink-dark: #222222;
    --text-on-green: #ffffff;
  }
  html, body {
    margin: 0;
    padding: 0;
    overflow: hidden;
    background: var(--card-white);
  }
  .business-card {
    position: relative;
    width: 1200px;
    height: 702px;
    background: var(--card-white);
    overflow: hidden;
    font-family: "Questrial", sans-serif;
  }
  .green-panel {
    position: absolute;
    inset: 0;
    width: 1200px;
    height: 702px;
  }
  .green-panel polygon { fill: var(--brand-green); }

  .brand {
    position: absolute;
    left: 53px;
    top: 212px;
    display: flex;
    align-items: center;
    gap: 22px;
  }
  .brand-dot {
    width: 84px;
    height: 84px;
    border-radius: 50%;
    background: var(--brand-green);
    flex: none;
  }
  .brand-name {
    margin: 0;
    font-weight: 400;
    color: var(--ink-dark);
    line-height: 1;
  }
  .brand-name .primary {
    display: block;
    font-size: 60px;
    letter-spacing: 1px;
  }
  .brand-name .secondary {
    display: block;
    margin-top: 6px;
    font-size: 22px;
    letter-spacing: 13px;
  }

  .contact {
    position: absolute;
    left: 719px;
    top: 346px;
    color: var(--text-on-green);
    font-style: normal;
    font-size: 26px;
    line-height: 33px;
  }
  .contact p { margin: 0; }
  .address { text-transform: uppercase; }
  .phones { margin-top: 42px !important; }
  .phones .label {
    display: inline-block;
    width: 62px;
  }
  .online { margin-top: 6px !important; line-height: 31px; }
</style>
</head>
<body>
  <main class="business-card">
    <svg class="green-panel" viewBox="0 0 1200 702" aria-hidden="true">
      <polygon points="808,41 1200,238 1200,702 774,702 532,577"/>
    </svg>

    <div class="brand">
      <span class="brand-dot" aria-hidden="true"></span>
      <h1 class="brand-name">
        <span class="primary">VERDANT LOOP</span>
        <span class="secondary">ADVISORS LLC</span>
      </h1>
    </div>

    <address class="contact">
      <p class="address">5374 Tillbury Fenwood Road<br>Larkfield, MD 20911</p>
      <p class="phones">
        <span class="label">TEL</span>: 240.555.0143<br>
        <span class="label">FAX</span>: 240.555.0187
      </p>
      <p class="online">
        www.verdantloopadvisors.example<br>
        sales@verdantloopadvisors.example
      </p>
    </address>
  </main>
</body>
</html>
```